Packaging and Insert Design for New Cocktail/Bar Set

We are launching a new product under our brand, Shakerline Guild, and require a design for the product packaging (2 packages - an inner cylinder tube and an outer box), as well as an insert.

(Note for reference - "mixology" is the art of cocktail making).

Our product is a cocktail set which will be sold on the USA Vendora site.

Our logo has already been designed - please refer to the attached files. I've attached various vector files of our logo.

The cocktail set will be packaged in a cylinder tube box.
Please see uploaded files for an image of the cylinder, as well as dimensions.
Dimensions are 37.68cm x 28cm (when the print design is laid flat).
The physical tube will be 28cm high and have a diameter of 12cm.
See uploaded file 'Dimensions - Cylinder Box' for details.

The cylinder box will be enclosed in an outer white box for protection. The outer white box will be a very basic box (i.e. not high quality) we are using just to make storage of individual units easier (and to protect the cylinder tube). It is unlikely that the outer box will be retained by the buyer. It will have a very clean, simple design. It will have our logo on the front and a barcode on the back (at the bottom).
Dimensions of the outer box are 28.5cm high and 12.5cm wide (tall and rectangular in shape).
See uploaded file 'Dimensions - White Outer Box & Paper Card' for details.

So to confirm we have 2 packages - the internal cylinder tube will have full branding, and this will then be placed in the white outer box with a simple design (logo only plus barcode at the back).

We also require a small insert to be designed (9.1cm x 5.5cm). We will include the insert in the package. The insert will have our logo and will provide the buyer with our contact details. The buyer will register their email address with us, in order to quality for warranty and a free e-book.

We need to finalise the content for the product insert, as well as the additional information to be printed on the cylinder tube.

In terms of design for the inner cylinder tube, we are leaning towards a more simple design, with our logo displayed on the front of the box.
We are open to ideas/suggestions though.

We have also uploaded an image of the cocktail set components which will form part of the set.
Updates

Target Market(s)

Our target market will be cocktail making enthusiasts/hobbyists and professionals. This includes people who would like to but a cocktail set to use at home, as well as professional bartenders.

Industry/Entity Type

Product

Colors

Designer to choose colors to be used in the design.

Requirements
Must have
• Preference is for a clean, professional looking design.
• Internal cylinder tube - full branding, incorporating logo on the front. Possibly also either a slogan e.g. "The Art of Cocktail Making' or details of the product e.g. "Cocktail Making Set' or similar.
• Outer white box - very simple design with logo to be displayed on the front of the packaging.
Should not have
• The design should not be too busy/complex. Not too much going on.

```html
<!DOCTYPE html>
<html lang="en">
<head>
<meta charset="utf-8">
<title>Shakerline Guild – Cylinder Tube Wrap</title>
<link rel="stylesheet" href="https://fonts.googleapis.com/css2?family=Roboto+Slab:wght@400;700&display=swap">
<style>
  :root {
    --backdrop: #ededed;
    --wrap-black: #262626;
    --silver-light: #e4e4e4;
    --silver-mid: #a9abad;
    --silver-dark: #6b6e71;
    --logo-silver: #c9cacc;
    --tagline-ink: #2b2b2b;
  }
  html, body {
    margin: 0;
    width: 1200px;
    height: 800px;
    overflow: hidden;
    background: var(--backdrop);
  }
  .canvas {
    position: relative;
    width: 1200px;
    height: 800px;
  }
  .tube-wrap {
    position: absolute;
    left: 102px;
    top: 30px;
    width: 996px;
    height: 740px;
    background: var(--wrap-black);
    overflow: hidden;
    box-shadow: 0 2px 10px rgba(0,0,0,0.12);
  }
  .tube-wrap svg {
    position: absolute;
    inset: 0;
  }
  .brand-lockup {
    position: absolute;
    left: 0;
    top: 250px;
    width: 996px;
    display: flex;
    flex-direction: column;
    align-items: center;
  }
  .brand-row {
    display: flex;
    align-items: center;
    gap: 22px;
  }
  .brand-dot {
    width: 34px;
    height: 34px;
    border-radius: 50%;
    background: var(--logo-silver);
  }
  .brand-name {
    font-family: "Roboto Slab", serif;
    font-weight: 400;
    font-size: 62px;
    letter-spacing: 10px;
    text-transform: uppercase;
    color: var(--logo-silver);
    margin: 0;
  }
  .brand-rule {
    margin-top: 18px;
    width: 520px;
    height: 2px;
    background: var(--logo-silver);
  }
  .tagline {
    position: absolute;
    right: 56px;
    bottom: 48px;
    margin: 0;
    font-family: "Roboto Slab", serif;
    font-weight: 700;
    font-size: 44px;
    line-height: 1.1;
    letter-spacing: 0;
    color: var(--tagline-ink);
  }
</style>
</head>
<body>
<main class="canvas">
  <section class="tube-wrap" aria-label="Cylinder tube print wrap">
    <svg width="996" height="740" viewBox="0 0 996 740" aria-hidden="true">
      <defs>
        <linearGradient id="silverTop" x1="0" y1="0" x2="1" y2="1">
          <stop offset="0" stop-color="#6b6e71"/>
          <stop offset="0.5" stop-color="#e4e4e4"/>
          <stop offset="1" stop-color="#a9abad"/>
        </linearGradient>
        <linearGradient id="silverBottom" x1="0" y1="0" x2="1" y2="0">
          <stop offset="0" stop-color="#a9abad"/>
          <stop offset="0.45" stop-color="#e4e4e4"/>
          <stop offset="0.75" stop-color="#a9abad"/>
          <stop offset="1" stop-color="#6b6e71"/>
        </linearGradient>
      </defs>
      <path class="band-top" d="M0 0 H520 Q300 90 0 270 Z" fill="url(#silverTop)"/>
      <path class="band-bottom" d="M996 330 V740 H230 Q620 470 996 330 Z" fill="url(#silverBottom)"/>
    </svg>
    <div class="brand-lockup">
      <div class="brand-row">
        <span class="brand-dot"></span>
        <h1 class="brand-name">Shakerline Guild</h1>
      </div>
      <div class="brand-rule"></div>
    </div>
    <p class="tagline">The Art of<br>Cocktail<br>Making</p>
  </section>
</main>
</body>
</html>
```